Teskar Business Cards

We need new Business Cards for our startup. It just launched.It is working in the high-end it-market. Specifically in the cloud area. We are a hybrid cloud company. The company logo is attached. We are a Swiss based company. Information visible on the card is: 1. Logo 2. Company Name: Teskar AG 3. Subtitle: Hybrid Clouds. 3. Name: Lukas Brenner 4. Adress: Holderweg 12a, 8462 Eglisau, Switzerland 5. Email: lukas@teskar.example. 6. Mobile: +41 79 304 62 18. It should be a grey/white design. Similar to the attached logo. It should have class, high-quality but not too much color and no gold used.

I forgot to add my Position. Please use Founder / CEO. thanks lukas

```html
<!DOCTYPE html>
<html lang="en">
<head>
<meta charset="utf-8">
<title>Teskar AG – Business Card</title>
<link rel="stylesheet" href="https://fonts.googleapis.com/css2?family=Open+Sans:wght@300;400&display=swap">
<style>
  :root {
    --backdrop: #1c1b1b;
    --frame: #5a5a5a;
    --panel-light: #fbfbfb;
    --panel-mid: #e9e9e9;
    --panel-edge: #d2d2d2;
    --ink: #333333;
    --ink-soft: #4a4a4a;
    --icon-bg: #3d3d3d;
    --icon-fg: #f2f2f2;
    --rule: #6a6a6a;
    --mark: #b9b9b9;
  }
  * { box-sizing: border-box; margin: 0; padding: 0; }
  html, body {
    width: 1200px;
    height: 799px;
    overflow: hidden;
    background: var(--backdrop);
    font-family: "Open Sans", "Segoe UI", sans-serif;
    color: var(--ink);
  }
  .business-card {
    position: absolute;
    left: 150px;
    top: 142px;
    width: 900px;
    height: 514px;
    background: var(--frame);
  }
  .card-panel {
    position: absolute;
    inset: 26px;
    background: radial-gradient(ellipse at 38% 18%, var(--panel-light) 0%, var(--panel-mid) 55%, var(--panel-edge) 100%);
    clip-path: polygon(0 0, 100% 0, 100% calc(100% - 46px), calc(100% - 46px) 100%, 0 100%);
  }
  .brand {
    position: absolute;
    left: 56px;
    top: 128px;
    display: flex;
    align-items: center;
    gap: 22px;
  }
  .brand-mark {
    width: 64px;
    height: 64px;
    flex: none;
    background: linear-gradient(135deg, #cfcfcf, var(--mark));
  }
  .brand-name {
    font-weight: 300;
    font-size: 26px;
    letter-spacing: 10px;
    color: var(--ink);
    white-space: nowrap;
  }
  .brand-tagline {
    font-weight: 300;
    font-size: 14px;
    letter-spacing: 3px;
    color: var(--ink-soft);
    margin-top: 4px;
    white-space: nowrap;
  }
  .divider {
    position: absolute;
    left: 434px;
    top: 70px;
    width: 2px;
    height: 250px;
    background: linear-gradient(to bottom, transparent, var(--rule) 20%, var(--rule) 80%, transparent);
  }
  .person {
    position: absolute;
    left: 470px;
    top: 78px;
  }
  .person-name {
    font-size: 34px;
    font-weight: 400;
    color: var(--ink);
    letter-spacing: 0.3px;
  }
  .person-role {
    font-size: 15px;
    font-weight: 300;
    color: var(--ink-soft);
    margin-top: 2px;
    letter-spacing: 1px;
  }
  .contact-list {
    list-style: none;
    margin-top: 26px;
  }
  .contact-item {
    display: flex;
    align-items: center;
    gap: 16px;
    font-size: 17px;
    color: var(--ink);
    margin-bottom: 22px;
  }
  .contact-icon {
    width: 24px;
    height: 24px;
    flex: none;
  }
  .address {
    position: absolute;
    left: 0;
    right: 0;
    top: 372px;
    text-align: center;
    font-size: 17px;
    letter-spacing: 2.2px;
    color: var(--ink-soft);
  }
</style>
</head>
<body>
  <article class="business-card">
    <div class="card-panel">
      <header class="brand">
        <div class="brand-mark" role="img" aria-label="Teskar AG company logo"></div>
        <div class="brand-text">
          <div class="brand-name">TESKAR AG</div>
          <div class="brand-tagline">Hybrid Clouds</div>
        </div>
      </header>
      <div class="divider"></div>
      <section class="person">
        <h1 class="person-name">Lukas Brenner</h1>
        <p class="person-role">Founder / CEO</p>
        <ul class="contact-list">
          <li class="contact-item">
            <svg class="contact-icon" viewBox="0 0 24 24" aria-hidden="true">
              <rect width="24" height="24" rx="4" fill="var(--icon-bg)"/>
              <path d="M8.5 5.5 L10.5 5.5 L11 9 L9.5 10 Q10.5 12.8 13.5 14.5 L14.5 13 L18 13.5 L18 15.5 Q17.5 18.5 15 18 Q7.5 16 6 8 Q6 5.5 8.5 5.5 Z" fill="var(--icon-fg)"/>
            </svg>
            <span>+41 79 304 62 18</span>
          </li>
          <li class="contact-item">
            <svg class="contact-icon" viewBox="0 0 24 24" aria-hidden="true">
              <rect width="24" height="24" rx="4" fill="var(--icon-bg)"/>
              <rect x="5" y="7" width="14" height="10" fill="none" stroke="var(--icon-fg)" stroke-width="1.4"/>
              <path d="M5 7 L12 13 L19 7" fill="none" stroke="var(--icon-fg)" stroke-width="1.4"/>
            </svg>
            <span>lukas@teskar.example</span>
          </li>
        </ul>
      </section>
      <p class="address">Holderweg 12a, 8462 Eglisau, Switzerland</p>
    </div>
  </article>
</body>
</html>
```